MODELS AGENCY NEW YEAR 2026 CARD

A 10 cm x 21 cm horizontal New Year card for clients of our 2 models agencies, Pommelin (kids) and Velvaride (actors and adults) (logo in the jobs).

Side A of the card: creative mission:
-text: 2026
-text: Peace and Love
-Studio or movie set atmosphere
-tone of voice: optimistic, positive, colorful

Side B:
(name of 4 people of the agency:)
Odette, Anne-Sophie, Hortense & Luc-Antoine,
(2 logos)
Pommelin & VelvaRide
(Adres)
Rue des Tilleuls 74 b3 - 1200 Bruxelles - Belgique

Target Market(s)

Movie directors, photographers

Industry/Entity Type

Fashion, advertising & Movies

Requirements
Must have
• SEE TEXT IN BRIEFING

```html
<!DOCTYPE html>
<html lang="fr">
<head>
<meta charset="utf-8">
<title>New Year 2026 Card – Velvaride &amp; Pommelin</title>
<link rel="stylesheet" href="https://fonts.googleapis.com/css2?family=Poppins:wght@500;600;700;800&family=Playfair+Display:wght@500&display=swap">
<style>
  :root {
    --page: #ffffff;
    --navy-deep: #05060f;
    --navy: #0e1430;
    --navy-glow: #17224a;
    --gold-light: #fbe27a;
    --gold: #e2b33c;
    --gold-dark: #b07c1c;
    --white: #ffffff;
    --photo-light: #c9c9c9;
    --photo-dark: #5e5e5e;
  }
  * { margin: 0; padding: 0; box-sizing: border-box; }
  html, body {
    width: 1200px; height: 1200px; overflow: hidden;
    background: var(--page);
    font-family: "Poppins", sans-serif;
  }
  .canvas { position: relative; width: 1200px; height: 1200px; }

  .card {
    position: absolute; left: 114px; width: 980px; height: 467px;
    overflow: hidden;
    background:
      radial-gradient(circle at 50% 35%, var(--navy-glow) 0%, transparent 55%),
      radial-gradient(ellipse at 50% 50%, var(--navy) 0%, var(--navy-deep) 100%);
    color: var(--white);
  }
  .card--front { top: 120px; }
  .card--back { top: 621px; }

  .decor {
    position: absolute; top: 0;
    background: radial-gradient(ellipse at 50% 40%, rgba(226,179,60,.35) 0%, rgba(176,124,28,.15) 45%, transparent 75%);
  }

  /* Front */
  .year {
    position: absolute; font-weight: 800; line-height: 1; font-size: 168px; letter-spacing: -6px;
    transform: scaleY(1.3); transform-origin: top left;
    background: linear-gradient(160deg, var(--gold-light) 10%, var(--gold) 50%, var(--gold-dark) 95%);
    -webkit-background-clip: text; background-clip: text; color: transparent;
  }
  .year--top { left: 358px; top: 32px; }
  .year--bottom { left: 430px; top: 105px; }
  .greeting {
    position: absolute; left: 0; right: 0; top: 296px; text-align: center;
    font-family: "Playfair Display", serif; font-weight: 500; font-size: 58px; letter-spacing: -1px;
  }
  .photo-frame { position: absolute; inset: 0; }

  .brand { position: absolute; text-align: center; white-space: nowrap; }
  .brand__name { display: block; font-weight: 600; font-size: 24px; line-height: 1; letter-spacing: 0.5px; color: var(--white); }
  .brand__tag { display: block; margin-top: 7px; font-weight: 500; font-size: 6px; letter-spacing: 0.8px; text-transform: uppercase; color: var(--white); }
  .brand-divider { position: absolute; left: 486px; top: 398px; width: 1.5px; height: 38px; background: var(--white); }

  .card--front .brand--actors { left: 326px; top: 401px; width: 144px; }
  .card--front .brand--kids { left: 500px; top: 401px; width: 144px; }
  .card--back .brand--actors { left: 300px; top: 66px; width: 180px; }
  .card--back .brand--kids { left: 494px; top: 66px; width: 180px; }
  .card--back .brand__name { font-size: 30px; }
  .card--back .brand__tag { font-size: 7px; letter-spacing: 1px; }

  /* Back */
  .team { position: absolute; left: 0; right: 0; top: 132px; text-align: center; list-style: none; }
  .team__name { font-weight: 700; font-size: 48px; line-height: 59px; text-transform: uppercase; letter-spacing: -0.5px; }
  .address {
    position: absolute; left: 181px; top: 389px; width: 610px; height: 39px; border-radius: 20px;
    background: linear-gradient(90deg, var(--gold-dark), var(--gold) 30%, var(--gold-light) 60%, var(--gold) 85%, var(--gold-dark));
    display: flex; align-items: center; justify-content: center;
    font-weight: 700; font-size: 19px; color: var(--white);
  }
</style>
</head>
<body>
<main class="canvas">

  <section class="card card--front">
    <div class="decor" style="left:0;width:245px;height:260px" role="img" aria-label="Hanging gold baubles, stars, snowflakes and streamers"></div>
    <div class="decor" style="left:722px;width:258px;height:260px" role="img" aria-label="Hanging gold baubles, stars, snowflakes and fireworks"></div>

    <svg class="photo-frame" width="980" height="467" viewBox="0 0 980 467">
      <defs>
        <linearGradient id="photoTone" x1="0" y1="0" x2="1" y2="1">
          <stop offset="0" stop-color="var(--photo-light)"/>
          <stop offset="1" stop-color="var(--photo-dark)"/>
        </linearGradient>
        <linearGradient id="goldArc" x1="0" y1="0" x2="1" y2="0">
          <stop offset="0" stop-color="var(--gold-dark)"/>
          <stop offset=".5" stop-color="var(--gold-light)"/>
          <stop offset="1" stop-color="var(--gold)"/>
        </linearGradient>
      </defs>
      <circle cx="140" cy="455" r="188" fill="none" stroke="url(#goldArc)" stroke-width="5"/>
      <circle cx="140" cy="455" r="181" fill="url(#photoTone)" role="img" aria-label="Black and white portrait of a smiling agency team member"/>
      <circle cx="840" cy="455" r="188" fill="none" stroke="url(#goldArc)" stroke-width="5"/>
      <circle cx="840" cy="455" r="181" fill="url(#photoTone)" role="img" aria-label="Black and white portrait of a thoughtful model"/>
    </svg>

    <span class="year year--top">20</span>
    <span class="year year--bottom">26</span>
    <p class="greeting">Peace &amp; Love</p>

    <div class="brand brand--actors">
      <span class="brand__name">Velvaride</span>
      <span class="brand__tag">People actors &amp; models agency</span>
    </div>
    <div class="brand-divider"></div>
    <div class="brand brand--kids">
      <span class="brand__name">Pommelin</span>
      <span class="brand__tag">Children models agency</span>
    </div>
  </section>

  <section class="card card--back">
    <div class="decor" style="left:0;width:290px;height:310px" role="img" aria-label="Hanging gold baubles, stars, snowflakes and streamers"></div>
    <div class="decor" style="left:690px;width:290px;height:310px" role="img" aria-label="Hanging gold baubles, stars, snowflakes and fireworks"></div>

    <div class="brand brand--actors">
      <span class="brand__name">Velvaride</span>
      <span class="brand__tag">People actors &amp; models agency</span>
    </div>
    <div class="brand brand--kids">
      <span class="brand__name">Pommelin</span>
      <span class="brand__tag">Children models agency</span>
    </div>

    <ul class="team">
      <li class="team__name">Odette</li>
      <li class="team__name">Anne-Sophie</li>
      <li class="team__name">Hortense</li>
      <li class="team__name">Luc-Antoine</li>
    </ul>

    <p class="address">Rue des Tilleuls 74 b3 - 1200 Bruxelles - Belgique</p>
  </section>

</main>
</body>
</html>
```